One Page / Executive Summary for Bright Harbor Executive Search

We would need an executive summary for our firm Bright Harbor Executive Search - like a small one pager which we can via PDF to our clients.
It should include like the file 23030 all Infos - Only Track Record needs to be complemented
But it should be designed much nicer than it is now - also open for new design situations but it should fit our website concept www.brightharbor.io
It should also include a graph of the recruiting process - maybe draw a new one.?
We would need a very elegant, modern, slim design, it should look very female - it should not have a green color block on the top but be more sleek bright and with our bird
Target Market(s)
CEO, HR executives
Industry/Entity Type
HR Consultantcy
Font styles to use
Other font styles liked:
- Calibri, cost or robotic condensed
Requirements
Must have
- sleek slim modern elegant design, ideally a white side with a frame or with our bird
Nice to have
- project progress on our website, female modern, elegant design, not too overloaded, possibility to complement our text
Should not have
- no petrol color block as on our website or as in our proposal, prefer a white background with our photo as a log,

```html
<!DOCTYPE html>
<html lang="en">
<head>
<meta charset="utf-8">
<title>Bright Harbor Executive Search – One Pager</title>
<link href="https://fonts.googleapis.com/css2?family=Poppins:wght@300;400;500;600;700&display=swap" rel="stylesheet">
<style>
:root{
  --red:#e0402f;
  --teal:#0f5a6e;
  --ink:#2f3335;
  --muted:#555b5e;
  --slate:#7f9cae;
  --pill:#d3e4ec;
  --wash:#b9d9e6;
  --backdrop:#eef0f1;
  --white:#ffffff;
}
*{box-sizing:border-box;margin:0;padding:0}
html,body{width:1200px;height:2400px;overflow:hidden}
body{background:var(--backdrop);font-family:'Poppins',sans-serif;color:var(--ink);position:relative}
.sheet{position:absolute;left:50px;top:423px;width:1100px;height:1553px;background:var(--white);box-shadow:0 20px 50px rgba(0,0,0,.12);overflow:hidden}
.abs{position:absolute}
.wash{right:0;top:0;width:620px;height:560px;background:radial-gradient(ellipse at 65% 40%,rgba(185,217,230,.75) 0%,rgba(185,217,230,.35) 40%,rgba(255,255,255,0) 70%)}
.brand{left:50px;top:120px;display:flex;align-items:center;gap:14px}
.brand-dot{width:18px;height:18px;border-radius:50%;background:var(--slate)}
.brand-name{font-weight:300;font-size:40px;letter-spacing:4px;color:var(--teal)}
.headline{left:50px;top:246px;font-size:33px;line-height:40px;font-weight:400;color:var(--ink)}
.tagline{left:50px;top:332px;font-size:37px;font-weight:700;color:var(--slate)}
.values{left:45px;top:420px;width:720px;height:80px}
.value{position:absolute;top:0;width:150px;text-align:center;transform:translateX(-50%)}
.value-icon{width:42px;height:42px;border-radius:50%;background:var(--pill);margin:0 auto;display:flex;align-items:center;justify-content:center}
.value-label{margin-top:10px;font-size:20px;color:var(--ink)}
.value-divider{position:absolute;top:4px;height:72px;border-left:1.5px dashed var(--pill)}
.rule{left:45px;top:518px;width:775px;height:2px;background:var(--red)}
.section-title{font-size:28px;font-weight:700;color:var(--red)}
.sub-title{font-size:18px;font-weight:600;color:var(--teal)}
.body-text{font-size:13.5px;line-height:16px;color:var(--muted)}
.services-title{left:50px;top:534px}
.exec{left:50px;top:566px;width:400px}
.advisory{left:594px;top:566px;width:455px}
.exec .body-text,.advisory .body-text{margin-top:6px}
.col-divider{left:512px;top:567px;height:119px;border-left:1px solid #ddd}
.why-title{left:50px;top:694px}
.why-lead{left:210px;top:713px;width:846px;height:189px;border-top:1.5px dashed var(--red);border-right:1.5px dashed var(--red);border-bottom:1.5px dashed var(--red);border-radius:0 12px 12px 0}
.why-lead::before{content:"";position:absolute;left:-6px;top:-4px;width:6px;height:6px;border-radius:50%;background:var(--red)}
.why-tail{left:57px;top:880px;width:153px;height:22px;border-left:1.5px dashed var(--red);border-bottom:1.5px dashed var(--red);border-radius:0 0 0 6px}
.why-item{position:absolute;display:flex;gap:8px;font-size:13.5px;line-height:16px;color:var(--muted)}
.why-item svg{flex:none;margin-top:2px}
.industries-title{left:50px;top:918px;font-size:32px}
.pill{position:absolute;top:927px;height:29px;border-radius:15px;background:var(--pill);font-size:16px;color:var(--ink);padding:4px 14px}
.process-title{left:50px;top:993px;font-size:28px;font-weight:600;color:var(--slate)}
.phase{position:absolute;top:1029px;font-size:12.5px;line-height:14px;color:var(--muted)}
.phase b{font-size:15px;font-weight:600;color:var(--ink);display:block}
.step{position:absolute;top:1102px;width:118px;border-left:1.5px solid #d0d5d8;padding-left:8px;height:130px}
.step-icon{width:30px;height:34px;margin-left:-9px;background:var(--teal);border-radius:50% 50% 50% 0;display:flex;align-items:center;justify-content:center}
.step h4{margin-top:10px;font-size:14.5px;font-weight:600;color:var(--red)}
.step p{font-size:11.5px;line-height:13.5px;color:var(--muted)}
.directors-title{left:717px;top:998px}
.portrait{position:absolute;border-radius:50%;border:3px solid var(--slate);background:linear-gradient(160deg,#e6ebee,#b6c2c8)}
.director-name{position:absolute;font-size:24px;font-weight:600;color:var(--ink)}
.director-role{position:absolute;font-size:15px;color:var(--ink)}
.numbers{left:0;top:1260px;width:555px;height:164px;background:var(--teal);border-radius:0 0 22px 0;color:var(--white)}
.numbers h3{position:absolute;left:50px;top:14px;font-size:25px;font-weight:600}
.stat{position:absolute;top:52px;border-left:1.5px dashed rgba(255,255,255,.6);padding-left:12px;font-size:15px;line-height:18px}
.stat strong{display:block;font-size:34px;line-height:36px;font-weight:700;color:var(--red)}
.track-title{left:594px;top:1280px;font-size:28px;font-weight:700;color:var(--teal)}
.track-box{left:602px;top:1299px;width:460px;height:168px;border-right:1.5px dashed var(--teal);border-bottom:1.5px dashed var(--teal);border-left:1.5px dashed var(--teal);border-radius:0 8px 8px 8px}
.track-top{left:802px;top:1299px;width:260px;border-top:1.5px dashed var(--teal)}
.track-box::before{content:"";position:absolute;left:-5px;top:36px;width:8px;height:8px;border-radius:50%;background:var(--teal)}
.locations{left:50px;top:1443px;display:flex;align-items:center;gap:22px;font-size:14px;font-weight:600;color:var(--ink)}
.locations .loc-title{font-size:19px;font-weight:500;color:var(--red);margin-right:-8px}
.loc{display:flex;align-items:center;gap:4px}
.contact-bar{left:37px;top:1478px;width:1036px;height:39px;border-radius:20px;background:linear-gradient(90deg,#dce9ef 0%,#e9f1f5 60%,var(--white) 70%);border:2px solid #e2ecf1;display:flex;align-items:center}
.contact-label{height:39px;margin:-2px 0 0 -2px;width:164px;background:var(--red);color:var(--white);border-radius:20px 0 0 20px;font-size:20px;font-weight:600;padding:5px 0 0 20px}
.contact-item{display:flex;align-items:center;gap:7px;font-size:18px;font-weight:500;color:var(--ink);margin-left:22px}
.contact-web{margin-left:auto;margin-right:24px;font-size:21px;font-weight:600;letter-spacing:7px;color:var(--teal)}
</style>
</head>
<body>
<main class="sheet">
  <div class="abs wash" role="img" aria-label="Soft pale blue decorative wash in the brand tones"></div>

  <header class="abs brand">
    <span class="brand-dot"></span>
    <span class="brand-name">BRIGHT HARBOR</span>
  </header>

  <h1 class="abs headline">So, they don’t wear<br>ties in the boardroom anymore.</h1>
  <p class="abs tagline">WE NEVER DID...</p>

  <section class="abs values">
    <div class="value" style="left:53px">
      <div class="value-icon"><svg width="20" height="18" viewBox="0 0 20 18"><path d="M10 17 2 9a4.5 4.5 0 0 1 8-5 4.5 4.5 0 0 1 8 5z" fill="#e0402f"/></svg></div>
      <div class="value-label">HONEST</div>
    </div>
    <div class="value-divider" style="left:128px"></div>
    <div class="value" style="left:210px">
      <div class="value-icon"><svg width="20" height="20" viewBox="0 0 20 20"><circle cx="10" cy="6" r="4.5" fill="#e0402f"/><path d="M2 19a8 7 0 0 1 16 0z" fill="#0f5a6e"/></svg></div>
      <div class="value-label">PERSONAL</div>
    </div>
    <div class="value-divider" style="left:306px"></div>
    <div class="value" style="left:397px">
      <div class="value-icon"><svg width="22" height="20" viewBox="0 0 22 20"><path d="M11 12 6 7a3 3 0 0 1 5-3 3 3 0 0 1 5 3z" fill="#e0402f"/><path d="M1 10l5 8h10l5-8" stroke="#0f5a6e" stroke-width="2.2" fill="none"/></svg></div>
      <div class="value-label">PRAGMATIC</div>
    </div>
    <div class="value-divider" style="left:510px"></div>
    <div class="value" style="left:575px">
      <div class="value-icon"><svg width="22" height="22" viewBox="0 0 22 22"><circle cx="11" cy="11" r="9" fill="#0f5a6e"/><path d="M5 7c3 0 4 2 3 5s2 4 3 7M13 3c0 3 2 3 4 3M14 11c2 0 4 1 5 3" stroke="#e0402f" stroke-width="2" fill="none"/></svg></div>
      <div class="value-label">DIVERSE</div>
    </div>
  </section>
  <div class="abs rule"></div>

  <h2 class="abs section-title services-title">Services</h2>
  <article class="abs exec">
    <h3 class="sub-title">Executive Search</h3>
    <p class="body-text">We are helping you to identify and hire highly qualified and experienced candidates for senior-level executive positions. Our goal is to identify the most qualified candidates and match them with the needs and culture of your company.</p>
  </article>
  <div class="abs col-divider"></div>
  <article class="abs advisory">
    <h3 class="sub-title">Advisory Leadership</h3>
    <p class="body-text">Our Leadership advisory’ services are _ for Management Teams as well as HR-Professionals and candidates. They are designed to help you, and your organization, to build strong and effective leadership skills and teams that can drive growth, innovation, and success.</p>
  </article>

  <h2 class="abs section-title why-title">Why Us?</h2>
  <div class="abs why-lead"></div>
  <div class="abs why-tail"></div>
  <div class="why-item" style="left:50px;top:752px;width:440px"><svg width="12" height="12" viewBox="0 0 12 12"><rect x=".5" y=".5" width="11" height="11" rx="2" fill="none" stroke="#e0402f"/><path d="M3 6l2 2 4-5" stroke="#e0402f" stroke-width="1.6" fill="none"/></svg><span>Longstanding experience with a passion for placing C-Level Executives</span></div>
  <div class="why-item" style="left:50px;top:798px;width:440px"><svg width="12" height="12" viewBox="0 0 12 12"><rect x=".5" y=".5" width="11" height="11" rx="2" fill="none" stroke="#e0402f"/><path d="M3 6l2 2 4-5" stroke="#e0402f" stroke-width="1.6" fill="none"/></svg><span>We work with you personally and act as an ambassador for our clients in the market</span></div>
  <div class="why-item" style="left:50px;top:845px;width:440px"><svg width="12" height="12" viewBox="0 0 12 12"><rect x=".5" y=".5" width="11" height="11" rx="2" fill="none" stroke="#e0402f"/><path d="M3 6l2 2 4-5" stroke="#e0402f" stroke-width="1.6" fill="none"/></svg><span>Engaging in at eye-level discussion beyond just placement and HR topics</span></div>
  <div class="why-item" style="left:550px;top:752px;width:470px"><svg width="12" height="12" viewBox="0 0 12 12"><rect x=".5" y=".5" width="11" height="11" rx="2" fill="none" stroke="#e0402f"/><path d="M3 6l2 2 4-5" stroke="#e0402f" stroke-width="1.6" fill="none"/></svg><span>Structured, lean and, most importantly, transparent’ digital processes, with the opportunity of 24/7 self-update on search status in our online tool</span></div>
  <div class="why-item" style="left:550px;top:813px;width:470px"><svg width="12" height="12" viewBox="0 0 12 12"><rect x=".5" y=".5" width="11" height="11" rx="2" fill="none" stroke="#e0402f"/><path d="M3 6l2 2 4-5" stroke="#e0402f" stroke-width="1.6" fill="none"/></svg><span>Creative search approaches and comprehensive candidate evaluation</span></div>
  <div class="why-item" style="left:550px;top:860px;width:470px"><svg width="12" height="12" viewBox="0 0 12 12"><rect x=".5" y=".5" width="11" height="11" rx="2" fill="none" stroke="#e0402f"/><path d="M3 6l2 2 4-5" stroke="#e0402f" stroke-width="1.6" fill="none"/></svg><span>Through referencing of candidates as part of the process; psychometrics on demand</span></div>

  <h2 class="abs section-title industries-title">Industries</h2>
  <span class="pill" style="left:249px;width:151px">Healthcare</span>
  <span class="pill" style="left:407px;width:193px">Private Capital</span>
  <span class="pill" style="left:605px;width:149px">Consumer</span>
  <span class="pill" style="left:761px;width:261px">Education &amp; Administration</span>

  <h2 class="abs process-title">Recruiting Process</h2>
  <div class="phase" style="left:50px"><b>Phase 1</b>Research-Longlist</div>
  <div class="phase" style="left:237px"><b>Phase 2</b>Fokus &amp; Interviews<br>Shortlist</div>
  <div class="phase" style="left:418px"><b>Phase 3</b>Abschluss</div>
  <svg class="abs" style="left:118px;top:1032px" width="310" height="10" viewBox="0 0 310 10">
    <path d="M0 5H112M187 5H296" stroke="#e0402f" stroke-width="1.2"/>
    <path d="M112 2l5 3-5 3zM296 2l5 3-5 3z" fill="#e0402f"/>
  </svg>

  <div class="step" style="left:50px"><div class="step-icon"><svg width="14" height="16" viewBox="0 0 14 16"><circle cx="8" cy="3" r="2" fill="#fff"/><path d="M3 15l3-6 3 2 1 4M6 9l1-4 4 3" stroke="#fff" stroke-width="1.6" fill="none"/></svg></div><h4>Kickoff</h4><p>bstimmung Profil, onsbeschreibung und Zielfirmenliste.</p></div>
  <div class="step" style="left:172px"><div class="step-icon"><svg width="14" height="14" viewBox="0 0 14 14"><circle cx="8" cy="6" r="4" stroke="#fff" stroke-width="1.6" fill="none"/><path d="M5 9l-4 4" stroke="#fff" stroke-width="2"/></svg></div><h4>Research</h4><p>Aktiver und passive Research, Ansprache pot. Kandidat*innen</p></div>
  <div class="step" style="left:289px"><div class="step-icon"><svg width="16" height="14" viewBox="0 0 16 14"><rect x="1" y="1" width="14" height="7" rx="1" fill="#fff"/><circle cx="5" cy="11" r="2" fill="#fff"/><circle cx="11" cy="11" r="2" fill="#fff"/></svg></div><h4>Interviews</h4><p>Prasentation der priorisierten Profile, Klienteninter-wiews</p></div>
  <div class="step" style="left:397px"><div class="step-icon" style="background:var(--pill)"><svg width="16" height="14" viewBox="0 0 16 14"><circle cx="5" cy="4" r="2.5" fill="#0f5a6e"/><circle cx="11" cy="4" r="2.5" fill="#0f5a6e"/><path d="M1 13a4 4 0 0 1 8 0zM7 13a4 4 0 0 1 8 0z" fill="#0f5a6e"/></svg></div><h4>Referenzen</h4><p>Ggf. Assessments, Einholen von Referenzen</p></div>
  <div class="step" style="left:519px;width:140px"><div class="step-icon"><svg width="16" height="14" viewBox="0 0 16 14"><circle cx="8" cy="4" r="2.5" fill="#fff"/><circle cx="3" cy="6" r="2" fill="#fff"/><circle cx="13" cy="6" r="2" fill="#fff"/><path d="M3 13a5 4 0 0 1 10 0z" fill="#fff"/></svg></div><h4>Kandidatenauswahl</h4><p>Vertragsverhandlung und Onboarding, Feedback-Gesprach</p></div>

  <h2 class="abs section-title directors-title">Managing Directors</h2>
  <div class="portrait" style="left:712px;top:1067px;width:86px;height:86px" role="img" aria-label="Portrait photo of managing director Dr. Clara Vensmoor Ried"></div>
  <div class="director-name" style="left:808px;top:1080px">Dr. Clara Vensmoor</div>
  <div class="director-role" style="left:808px;top:1114px">Ried</div>
  <div class="portrait" style="left:711px;top:1178px;width:92px;height:92px" role="img" aria-label="Portrait photo of managing director Lena Farrow"></div>
  <div class="director-name" style="left:815px;top:1206px">Lena Farrow</div>

  <section class="abs numbers">
    <h3>By The Numbers</h3>
    <div class="stat" style="left:50px"><strong>95%</strong>retention rate<br>over the course<br>of two years</div>
    <div class="stat" style="left:206px"><strong>30</strong>placements<br>made with<br>Bright Harbor</div>
    <div class="stat" style="left:354px"><strong>In total<br>20 years</strong>of experience in the<br>Executive search sector</div>
  </section>

  <h2 class="abs track-title">Track Record</h2>
  <div class="abs track-top"></div>
  <div class="abs track-box" style="border-top:none"></div>

  <div class="abs locations">
    <span class="loc-title">LOCATION</span>
    <span class="loc"><svg width="11" height="15" viewBox="0 0 11 15"><path d="M5.5 14C2 9 1 7 1 5.5a4.5 4.5 0 0 1 9 0C10 7 9 9 5.5 14z" fill="#e0402f"/><circle cx="5.5" cy="5.5" r="1.8" fill="#fff"/></svg>HAMBURG</span>
    <span class="loc"><svg width="11" height="15" viewBox="0 0 11 15"><path d="M5.5 14C2 9 1 7 1 5.5a4.5 4.5 0 0 1 9 0C10 7 9 9 5.5 14z" fill="#e0402f"/><circle cx="5.5" cy="5.5" r="1.8" fill="#fff"/></svg>WIEN</span>
    <span class="loc"><svg width="11" height="15" viewBox="0 0 11 15"><path d="M5.5 14C2 9 1 7 1 5.5a4.5 4.5 0 0 1 9 0C10 7 9 9 5.5 14z" fill="#e0402f"/><circle cx="5.5" cy="5.5" r="1.8" fill="#fff"/></svg>MUNCHEN</span>
    <span class="loc"><svg width="11" height="15" viewBox="0 0 11 15"><path d="M5.5 14C2 9 1 7 1 5.5a4.5 4.5 0 0 1 9 0C10 7 9 9 5.5 14z" fill="#e0402f"/><circle cx="5.5" cy="5.5" r="1.8" fill="#fff"/></svg>DUSSELDORF</span>
  </div>

  <footer class="abs contact-bar">
    <span class="contact-label">Contact Us</span>
    <span class="contact-item"><svg width="18" height="18" viewBox="0 0 18 18"><path d="M4 1l3 4-2 2c1 2 3 4 5 5l2-2 4 3-2 3C8 16 2 10 1 4z" fill="#0f5a6e"/></svg>055501/2468</span>
    <span class="contact-item" style="margin-left:30px"><svg width="18" height="13" viewBox="0 0 18 13"><rect x=".5" y=".5" width="17" height="12" fill="#0f5a6e"/><path d="M1 1l8 6 8-6" stroke="#fff" stroke-width="1.3" fill="none"/></svg>office@brightharbor.io</span>
    <span class="contact-web">www.brightharbor.io</span>
  </footer>
</main>
</body>
</html>
```